Whitening Flyer

I need an informational flyer for my dental practice. The flyer will describe the whitening services that are available at my practice and show price of each whitening service. We currently gave a 3 fold brochure, but I prefer something with a more professional look, and personalized with our branding and practice colors. I have attached the current flyer for you to use similar text. I will also attach a flyer that I have used in the past that could demonstrate my branding or feel free to view my website: www.grkvemu.com

```html
<!DOCTYPE html>
<html lang="en">
<head>
<meta charset="utf-8">
<title>Brightline Dental – Whitening Brochure</title>
<link rel="stylesheet" href="https://fonts.googleapis.com/css2?family=Montserrat:wght@400;600;700;900&family=Bebas+Neue&family=Satisfy&display=swap">
<style>
  :root{
    --red:#e4202a;
    --white:#ffffff;
    --ink:#2b2b2b;
    --stage:#d7d7d9;
    --photo-warm:#c9a48a;
    --photo-pink:#e6a6ae;
    --photo-studio:#cfc7c2;
  }
  *{box-sizing:border-box;margin:0;padding:0}
  html,body{width:840px;height:1200px;overflow:hidden}
  body{background:var(--stage);font-family:'Montserrat',sans-serif;color:var(--ink);position:relative}

  .sheet{position:absolute;left:50px;width:740px;height:572px;background:var(--white);overflow:hidden;box-shadow:0 4px 14px rgba(0,0,0,.18)}
  .sheet--outside{top:18px}
  .sheet--inside{top:610px}
  .panel{position:absolute;top:0;height:100%}

  /* outside: getting started */
  .panel--start{left:0;width:247px;padding:40px 34px 0 27px}
  .section-title{font-weight:900;color:var(--red);font-size:22px;line-height:21px;letter-spacing:.2px}
  .copy{font-size:10.3px;line-height:14.2px;color:var(--ink)}
  .panel--start .copy{margin-top:17px}
  .factors{list-style:none;margin-top:15px}
  .factors li{display:flex;font-size:10.3px;line-height:14.2px;margin-bottom:14px}
  .factors .num{color:var(--red);font-weight:700;width:17px;flex:none}
  .factors b{color:var(--red);font-weight:700}

  /* outside: contact */
  .panel--contact{left:247px;width:246px;background:var(--red);color:var(--white)}
  .snapshot{position:absolute;background:var(--white);padding:5px;box-shadow:3px 5px 10px rgba(0,0,0,.35)}
  .snapshot .photo{width:100%;height:100%}
  .snapshot--group{left:2px;top:78px;width:210px;height:170px;transform:rotate(-6deg)}
  .snapshot--pair{left:50px;top:238px;width:200px;height:152px;transform:rotate(5deg)}
  .contact{position:absolute;left:0;right:0;top:440px;text-align:center;font-size:9px;line-height:13px}
  .contact h3{font-size:9px;font-weight:700;margin-bottom:8px}
  .contact strong{font-weight:700}
  .social{position:absolute;left:66px;top:529px;font-size:7.5px;font-weight:700;line-height:16px}
  .social span{display:flex;align-items:center;gap:7px}
  .social i{width:7px;height:7px;border-radius:50%;background:var(--white);display:inline-block}

  /* outside: cover */
  .panel--cover{left:493px;width:247px}
  .brand{font-weight:600;color:var(--red);font-size:13px;display:flex;align-items:center;gap:5px}
  .brand i{width:8px;height:8px;border-radius:50%;background:var(--red);display:inline-block}
  .panel--cover .brand{position:absolute;right:14px;top:30px}
  .cover-photo{position:absolute;left:0;right:0;top:190px;height:327px;background:linear-gradient(180deg,#fff 0%,var(--photo-warm) 55%,#f3eee9 100%)}
  .cover-title{position:absolute;left:23px;top:66px;font-family:'Bebas Neue',sans-serif;color:var(--red);font-size:50px;line-height:42px;letter-spacing:.5px}
  .cover-band{position:absolute;left:0;right:0;bottom:0;height:55px;background:var(--red);color:var(--white);text-align:center;padding-top:8px}
  .cover-band .lead{font-size:8.5px;font-weight:700}
  .cover-band .script{font-family:'Satisfy',cursive;font-size:20px;line-height:22px}

  /* inside */
  .team-photo{position:absolute;left:0;top:0;width:493px;height:299px;background:linear-gradient(180deg,#dcd6d2 0%,var(--photo-studio) 50%,#b8876a 100%)}
  .brand-badge{position:absolute;left:175px;top:270px;width:145px;height:58px;border-radius:50%;background:var(--white);display:flex;justify-content:center;padding-top:14px}
  .why{position:absolute;left:27px;top:316px;width:190px}
  .why .copy p{margin-bottom:14px}
  .why .copy{margin-top:12px}
  .tagline{position:absolute;right:264px;top:337px;text-align:right}
  .tagline .lead{font-size:12px;font-weight:600;color:var(--ink)}
  .tagline .big{font-weight:900;color:var(--red);font-size:49px;line-height:39px;letter-spacing:-1px;margin-top:6px}
  .panel--packages{left:493px;width:247px;background:var(--red);color:var(--white);padding:46px 30px 0 44px}
  .package{margin-bottom:13px}
  .package h4{font-size:10.3px;font-weight:700;line-height:14px;margin-bottom:3px}
  .package p{font-size:10.2px;line-height:14.2px}
</style>
</head>
<body>

<section class="sheet sheet--outside">
  <div class="panel panel--start">
    <h2 class="section-title">How do you<br>Get started?</h2>
    <p class="copy">There are many options and factors to take into account when deciding which whitening option is best for you. Our team is here to help you in the decision process. Some deciding factors include:</p>
    <ol class="factors">
      <li><span class="num">1.</span><span><b>The cost:</b> cost range anywhere from $30 for over the counter treatment to $600 for some in office treatments.</span></li>
      <li><span class="num">2.</span><span><b>The Effort:</b> in office treatment can take as little time as 1 ½ hours where as over the counter treatment can take up to 3 weeks to see a difference.</span></li>
      <li><span class="num">3.</span><span><b>The Sensitivity:</b> if you suffer from sensitive gums or teeth some of thr stroner treatments may not be the best option for you.</span></li>
      <li><span class="num">4.</span><span><b>The Results:</b> There is a significant difference in the active whitening ingredient that is allowed in OTC products vs in office solutions. Typically; a professional solution will make your teeth brighter, faster.</span></li>
    </ol>
  </div>

  <div class="panel panel--contact">
    <div class="snapshot snapshot--group"><div class="photo" role="img" aria-label="Group of smiling friends in colourful shirts" style="background:linear-gradient(160deg,#f1efec,#e7b089 60%,#e0c35a)"></div></div>
    <div class="snapshot snapshot--pair"><div class="photo" role="img" aria-label="Smiling couple taking a selfie on a pink backdrop" style="background:linear-gradient(150deg,var(--photo-pink),#d9b6a8 60%,#f4f0ee)"></div></div>
    <div class="contact">
      <h3>Contact us</h3>
      <strong>Brightline Dental</strong><br>
      1420 Harbor Ave, Marlow, LA. 70555<br>
      (555) 014-2290 &nbsp;|&nbsp; info@grkvemu.com<br>
      www.grkvemu.com
    </div>
    <div class="social">
      <span><i></i>brightline_dental_studio</span>
      <span><i></i>Brightline Dental</span>
    </div>
  </div>

  <div class="panel panel--cover">
    <div class="cover-photo" role="img" aria-label="Laughing woman standing behind a laughing man"></div>
    <div class="brand"><i></i>Brightline Dental</div>
    <h1 class="cover-title">WHICH<br>WHITENING<br>IS RIGHT?</h1>
    <div class="cover-band">
      <div class="lead">At Brightline Dental,</div>
      <div class="script">we care about your smile</div>
    </div>
  </div>
</section>

<section class="sheet sheet--inside">
  <div class="team-photo" role="img" aria-label="Diverse group of smiling adults posing together"></div>
  <div class="brand-badge"><div class="brand"><i></i>Brightline Dental</div></div>
  <div class="why">
    <h2 class="section-title">Why Us?</h2>
    <div class="copy">
      <p>Our office staff has been trained extensively to assist you step by step in the whitening process. From pre-op to post op, they are by your side to help with questions or concerns.</p>
      <p>Our office offers multiple options fitting every budget. You can also speak with our office manager about possible payment options.</p>
      <p>Some restrictions may apply and results.</p>
    </div>
  </div>
  <div class="tagline">
    <div class="lead">At Brightline Dental</div>
    <div class="big">We<br>care<br>about<br>your<br>smile</div>
  </div>

  <div class="panel panel--packages">
    <div class="package"><h4>Basic Whitening Package</h4><p>$10 One Upper and Lower one-time use tray set and care instructions. No appointment needed.</p></div>
    <div class="package"><h4>Silver Whitening Package</h4><p>$80 Ten Upper and Lower one-time use trays and care instructions. No appointment needed.</p></div>
    <div class="package"><h4>Gold Whitening Package</h4><p>$275 Custom made upper and lower whitening trays to be used at home. One 30 min office appointment for impressions. 4 tubes of professional whitening agent. At home care instructions (refills available for purchase of $35)</p></div>
    <div class="package"><h4>Diamond Whitening Package</h4><p>$375 One 90 min office appointment for chairside lumivance whitening. At home care instructions.</p></div>
    <div class="package"><h4>Platinum Whitening Package</h4><p>$475 One 2hr office appoinment for chairside lumivance whitening. At home care instructions.</p></div>
  </div>
</section>

</body>
</html>
```